Larvik Consulting

Hi,
I have my own network consulting business (just me)
and need to get a logo and business card design together,

Based in New Zealand,

Tobias Wrenfield
Unified Communications and Network Architect

/design engineer,
and would like this to be the basis for personal branding and company identity

Industry/Entity Type

Business

Requirements
Nice to have
• I have the basis for a optional logo - needs color -

```html
<!DOCTYPE html>
<html lang="en">
<head>
<meta charset="utf-8">
<title>Tobias Wrenfield – Business Cards</title>
<link rel="stylesheet" href="https://fonts.googleapis.com/css2?family=Marcellus&family=Open+Sans:wght@400;600&display=swap">
<style>
  :root {
    --backdrop: #1c1c1c;
    --card-white: #ffffff;
    --blue-light: #6cc6e0;
    --blue-mid: #3f8fd0;
    --blue-deep: #3a3fa8;
    --violet: #3a2590;
    --brand-blue: #2f7fc1;
    --ink: #1d1d2b;
    --ink-soft: #444448;
  }
  * { margin: 0; padding: 0; box-sizing: border-box; }
  html, body { width: 1200px; height: 887px; overflow: hidden; }
  body {
    position: relative;
    background: var(--backdrop);
    font-family: "Open Sans", sans-serif;
  }
  .card {
    position: absolute;
    width: 525px;
    height: 298px;
    border-radius: 18px;
    overflow: hidden;
  }
  .card--front {
    top: 160px;
    background:
      radial-gradient(ellipse 70% 95% at 42% 55%, var(--blue-light) 0%, var(--blue-mid) 40%, var(--blue-deep) 80%, var(--violet) 100%);
  }
  .card--front-a { left: 85px; }
  .card--front-b { left: 623px; }
  .card--back {
    left: 87px;
    top: 476px;
    height: 299px;
    background: var(--card-white);
  }

  .front-mark {
    position: absolute;
    left: 333px;
    top: 112px;
    width: 80px;
    height: 80px;
    border-radius: 50%;
    background: #ffffff;
  }
  .front-name {
    position: absolute;
    right: 30px;
    top: 236px;
    font-family: "Marcellus", serif;
    font-size: 29px;
    line-height: 1;
    color: #ffffff;
    letter-spacing: 0.2px;
    white-space: nowrap;
  }
  .front-tagline {
    position: absolute;
    right: 31px;
    top: 271px;
    font-size: 11.5px;
    color: #ffffff;
    white-space: nowrap;
  }

  .back-mark {
    position: absolute;
    left: 30px;
    top: 38px;
    width: 56px;
    height: 56px;
    border-radius: 50%;
    background: var(--brand-blue);
  }
  .back-name {
    position: absolute;
    left: 103px;
    top: 56px;
    font-family: "Marcellus", serif;
    font-size: 25px;
    line-height: 1;
    color: var(--ink);
    white-space: nowrap;
  }
  .back-tagline {
    position: absolute;
    left: 103px;
    top: 85px;
    font-size: 10.5px;
    color: var(--ink);
    white-space: nowrap;
  }
  .address {
    position: absolute;
    left: 36px;
    top: 150px;
    font-size: 13px;
    line-height: 19px;
    color: var(--ink-soft);
    font-style: normal;
  }
  .contacts {
    position: absolute;
    left: 36px;
    top: 201px;
    list-style: none;
    font-size: 13px;
    color: var(--ink-soft);
  }
  .contacts li {
    display: flex;
    align-items: center;
    height: 19.5px;
  }
  .contacts svg {
    width: 11px;
    height: 11px;
    margin-right: 9px;
    fill: var(--brand-blue);
  }
  .person {
    position: absolute;
    right: 41px;
    top: 178px;
    text-align: right;
  }
  .person-name {
    font-size: 17px;
    font-weight: 600;
    color: var(--brand-blue);
    line-height: 22px;
  }
  .person-role {
    font-size: 14px;
    color: var(--ink-soft);
    line-height: 20px;
  }
</style>
</head>
<body>
  <section class="card card--front card--front-a">
    <div class="front-mark"></div>
    <p class="front-name">TOBIAS WRENFIELD</p>
    <p class="front-tagline">Unified Communications and Network Architect</p>
  </section>

  <section class="card card--front card--front-b">
    <p class="front-name">TOBIAS WRENFIELD</p>
    <p class="front-tagline">Unified Communications and Network Architect</p>
  </section>

  <section class="card card--back">
    <div class="back-mark"></div>
    <p class="back-name">TOBIAS WRENFIELD</p>
    <p class="back-tagline">Unified Communications and Network Architect</p>

    <address class="address">8 Harbour Lane,<br>Auckland 1010 New Zealand</address>

    <ul class="contacts">
      <li>
        <svg viewBox="0 0 12 12" aria-hidden="true"><path d="M1 3.5C1 2 2.5 1.5 6 1.5S11 2 11 3.5v1H8.5V3.6H3.5v.9H1zM3 5h6l2 5H1z"/></svg>
        021 555 0148
      </li>
      <li>
        <svg viewBox="0 0 12 12" aria-hidden="true"><rect x="1" y="8" width="2" height="3"/><rect x="4" y="6" width="2" height="5"/><rect x="7" y="4" width="2" height="7"/><rect x="10" y="1" width="2" height="10"/></svg>
        021 555 0148
      </li>
      <li>
        <svg viewBox="0 0 12 12" aria-hidden="true"><path d="M1 2.5h10v7H1zM2 3.5v.3L6 6.6l4-2.8v-.3zm0 1.5v3.5h8V5L6 7.8z" fill-rule="evenodd"/></svg>
        tobias@tobiaswrenfield.com
      </li>
      <li>
        <svg viewBox="0 0 12 12" aria-hidden="true"><path d="M6 1a5 5 0 1 0 0 10A5 5 0 0 0 6 1zm-.6 1.2v3.2H2.2a4 4 0 0 1 3.2-3.2zm1.2 0a4 4 0 0 1 3.2 3.2H6.6zM2.2 6.6h3.2v3.2a4 4 0 0 1-3.2-3.2zm4.4 0h3.2a4 4 0 0 1-3.2 3.2z"/></svg>
        www.tobiaswrenfield.com
      </li>
    </ul>

    <div class="person">
      <p class="person-name">Tobias Wrenfield</p>
      <p class="person-role">Design Engineer</p>
    </div>
  </section>
</body>
</html>
```